Book Cover design: Waltz with a Heron.

I need a front and back cover for my book called 'Waltz with a Heron'.
It is self development book for help a person to be a better coach.
It is a metaphor. Dance is asking questions and the octopus is the person you are coaching (complex with my 'tentacles').
The audience would be adults. so want the cover to capture attention and also show that is have something of interest inside.
I have attach my first attempt. Please be bold.
The best sellers in this market place have simple but clear front page & back pages.

All the words are important but the sub-title is likely to change.

Target Market(s)

Adults who work with each other.
More business type people.

Industry/Entity Type

Leadership

Font styles to use
Serif

Requirements
Must have
• My project must have... The words that in the draft mock up.
• 'Waltz with a Heron' [TITLE]
• 'A Path to True Mentoring'[SUB-TITLE]
• How to create inspiration and accountability using
• Seven Pivotal Turns.[SUB_TITLE]
• By Rowan P Thistlewood
Nice to have
• Clever and simple.

```html
<!DOCTYPE html>
<html lang="en">
<head>
<meta charset="utf-8">
<title>Waltz with a Heron — Book Cover</title>
<link rel="stylesheet" href="https://fonts.googleapis.com/css2?family=Gelasio:wght@400;600;700&family=Oswald:wght@600&display=swap">
<style>
  :root {
    --page: #ffffff;
    --cover: #a6847a;
    --ink-light: #ffffff;
    --ink-dark: #4b4b4b;
    --art-blue: #b6d3ee;
    --art-blue-soft: #9fc1e2;
  }
  html, body {
    margin: 0;
    padding: 0;
    width: 1200px;
    height: 933px;
    overflow: hidden;
    background: var(--page);
  }
  .canvas {
    position: relative;
    width: 1200px;
    height: 933px;
    background: var(--page);
  }
  .cover {
    position: absolute;
    top: 72px;
    width: 569px;
    height: 804px;
    background: var(--cover);
  }
  .cover--front { left: 24px; }
  .cover--back { left: 605px; }

  .author {
    position: absolute;
    left: 104px;
    top: 16px;
    margin: 0;
    font-family: "Oswald", "Arial Narrow", sans-serif;
    font-weight: 600;
    font-size: 28px;
    letter-spacing: 0.4px;
    color: var(--ink-dark);
  }
  .tagline {
    position: absolute;
    left: 62px;
    top: 104px;
    margin: 0;
    font-family: "Gelasio", Georgia, serif;
    font-size: 22px;
    color: var(--ink-light);
  }
  .title {
    position: absolute;
    left: 0;
    top: 140px;
    margin: 0;
    font-family: "Gelasio", Georgia, serif;
    font-weight: 600;
    color: var(--ink-light);
    line-height: 1;
  }
  .title__line { position: absolute; white-space: nowrap; }
  .title__line--first { left: 72px; top: 0; font-size: 86px; }
  .title__line--joiner { left: 212px; top: 84px; font-size: 33px; }
  .title__line--last { left: 88px; top: 118px; font-size: 86px; }

  .illustration {
    position: absolute;
    display: block;
  }
  .illustration--front { left: 171px; top: 370px; width: 255px; height: 195px; }
  .illustration--back { left: 292px; top: 580px; width: 265px; height: 203px; }

  .promise {
    position: absolute;
    left: 33px;
    top: 708px;
    margin: 0;
    font-family: "Gelasio", Georgia, serif;
    font-weight: 600;
    font-size: 18px;
    line-height: 23px;
    letter-spacing: 1.6px;
    word-spacing: 4px;
    text-transform: uppercase;
    color: var(--ink-light);
  }
</style>
</head>
<body>
  <div class="canvas">
    <section class="cover cover--front" aria-label="Front cover">
      <p class="author">ROWAN P THISTLEWOOD</p>
      <p class="tagline">'A Path to True Mentoring'</p>
      <h1 class="title">
        <span class="title__line title__line--first">WALTZ</span>
        <span class="title__line title__line--joiner">WITH A</span>
        <span class="title__line title__line--last">HERON</span>
      </h1>
      <svg class="illustration illustration--front" viewBox="0 0 255 195" role="img" aria-label="Light blue line illustration of the book's mascot animal, tentacles spread">
        <defs>
          <linearGradient id="art-front" x1="0" y1="0" x2="1" y2="1">
            <stop offset="0%" stop-color="var(--art-blue)"/>
            <stop offset="100%" stop-color="var(--art-blue-soft)"/>
          </linearGradient>
        </defs>
        <rect x="2" y="2" width="251" height="191" rx="28" fill="url(#art-front)" fill-opacity="0.55" stroke="var(--art-blue)" stroke-width="2"/>
      </svg>
      <p class="promise">How to create<br>inspiration and accountability<br>using seven pivotal coaching turns</p>
    </section>

    <section class="cover cover--back" aria-label="Back cover">
      <svg class="illustration illustration--back" viewBox="0 0 265 203" role="img" aria-label="Repeat of the light blue mascot line illustration">
        <defs>
          <linearGradient id="art-back" x1="0" y1="0" x2="1" y2="1">
            <stop offset="0%" stop-color="var(--art-blue)"/>
            <stop offset="100%" stop-color="var(--art-blue-soft)"/>
          </linearGradient>
        </defs>
        <rect x="2" y="2" width="261" height="199" rx="28" fill="url(#art-back)" fill-opacity="0.55" stroke="var(--art-blue)" stroke-width="2"/>
      </svg>
    </section>
  </div>
</body>
</html>
```